Redesign of our plinketra.com VPS mini site

We need to a full redesign (modern, fancy and attractive) with a new logo. The site is http://www.plinketra.com/

We are open to any idea / suggestion. Content will not be much more than what is present on the actual web site. We would like to see more filler images inside the page.

Into the attached files I've included all the current web pages

Target Market(s)

Internet Hosting

Industry/Entity Type

Internet Service Provider

Logo Text

Vemply Plinketra

Coding

Coded - Design and coding required

Number of Pages Required

3 page

Font styles to use
Sans Serif

```html
<!DOCTYPE html>
<html lang="en">
<head>
<meta charset="utf-8">
<title>Vemply Plinketra – VPS Hosting</title>
<link href="https://fonts.googleapis.com/css2?family=Open+Sans:wght@400;600;700;800&display=swap" rel="stylesheet">
<style>
:root{
  --gold:#d4a21a;
  --ink:#333;
  --text:#555;
  --muted:#888;
  --line:#e6e6e6;
  --grey-btn:#a9a9a9;
  --plans-bg:#f0f0f0;
  --footer:#1b1b1b;
  --footer-line:#3a3a3a;
  --dark-btn:#2a2420;
  --hero-dark:#1f3356;
}
*{box-sizing:border-box;margin:0;padding:0}
html,body{width:700px;height:1200px;overflow:hidden;background:#fff}
body{position:relative;font-family:"Open Sans",Arial,sans-serif;color:var(--text)}
/* header */
.site-header{position:absolute;left:0;top:0;width:700px;height:68px;border-top:2px solid var(--gold);background:#fff}
.brand{position:absolute;left:57px;top:22px;display:flex;align-items:center;gap:6px;font-size:14px;font-weight:700;color:var(--ink);white-space:nowrap}
.brand-mark{width:12px;height:12px;background:var(--gold)}
.topbar{position:absolute;right:52px;top:11px;font-size:7.5px;color:var(--muted);display:flex;gap:10px;white-space:nowrap}
.topbar .support{color:var(--ink)}
.topbar .support span{color:var(--muted)}
.main-nav{position:absolute;right:248px;top:39px;display:flex;gap:12px;font-size:7px;font-weight:600;color:var(--ink);white-space:nowrap}
.search-field{position:absolute;left:463px;top:36px;width:130px;height:18px;background:#f6f6f6}
.search-btn{position:absolute;left:594px;top:36px;width:53px;height:18px;background:var(--dark-btn);color:#fff;font-size:7.5px;text-align:center;line-height:18px}
/* hero */
.hero{position:absolute;left:0;top:68px;width:700px;height:238px;background:var(--hero-dark)}
.hero-photo{position:absolute;left:90px;top:0;width:504px;height:238px;background:linear-gradient(90deg,#14264a 0%,#2d4e82 25%,#a9b8cc 50%,#2d4e82 75%,#14264a 100%)}
.hero-caption{position:absolute;left:180px;top:179px;width:330px;height:32px;background:rgba(20,24,34,.85);color:#fff;font-size:8.5px;font-weight:700;text-align:center;line-height:32px;white-space:nowrap}
.hero-dots{position:absolute;left:338px;top:229px;display:flex;gap:3px}
.hero-dots i{width:6px;height:6px;border:1px solid #fff;border-radius:50%}
.hero-dots i.on{background:#3c6bb0}
/* welcome */
.section-title{position:absolute;left:0;width:700px;text-align:center;font-size:12.5px;font-weight:700;color:var(--ink);letter-spacing:.3px}
.welcome-text{position:absolute;left:68px;top:346px;width:574px;text-align:center;font-size:6.6px;line-height:11.5px;color:var(--text)}
.spec{position:absolute;top:396px;width:80px;text-align:center;font-size:8.5px;color:var(--text);white-space:nowrap}
.spec svg{display:block;margin:0 auto 8px}
/* features */
.laptop-art{position:absolute;left:26px;top:491px;width:331px;height:190px;background:linear-gradient(135deg,#e8e8e8,#cfd3d8);border-radius:6px}
.features-title{position:absolute;left:366px;top:490px;font-size:12px;font-weight:700;color:var(--ink)}
.features-intro{position:absolute;left:366px;top:513px;width:280px;font-size:6.6px;line-height:11.5px}
.feature-list{position:absolute;top:541px;list-style:none;font-size:7.2px;color:var(--ink);white-space:nowrap}
.feature-list li{height:18px;padding-left:15px;position:relative}
.feature-list li::before{content:"";position:absolute;left:0;top:3px;width:3px;height:3px;border-radius:50%;background:#777}
/* plans */
.plans{position:absolute;left:0;top:711px;width:700px;height:316px;background:var(--plans-bg)}
.plan-card{position:absolute;top:48px;width:131px;height:238px;background:#fff;text-align:center}
.price{margin-top:10px;font-size:24px;font-weight:800;color:#3a4250;line-height:26px}
.price sup{font-size:17px;font-weight:400;vertical-align:2px}
.per{font-size:6.8px;letter-spacing:1px;color:#3a4250}
.plan-name{width:92px;height:18px;margin:14px auto 24px;background:var(--grey-btn);color:#fff;font-size:6.6px;font-weight:700;letter-spacing:.8px;line-height:18px}
.perks{list-style:none;width:108px;margin:0 auto;font-size:6.8px;color:var(--muted)}
.perks li{height:20px;line-height:20px;border-bottom:1px solid var(--line)}
.perks li:first-child{border-top:1px solid var(--line)}
.perks li:last-child{border-bottom:0}
.signup{width:58px;height:21px;margin:14px auto 0;background:var(--grey-btn);color:#fff;font-size:6.6px;font-weight:700;letter-spacing:.8px;line-height:21px}
.plan-card.gold .price,.plan-card.gold .per{color:var(--gold)}
.plan-card.gold .plan-name,.plan-card.gold .signup{background:var(--gold)}
/* footer */
.site-footer{position:absolute;left:0;top:1027px;width:700px;height:173px;background:var(--footer);color:#aaa}
.footer-col{position:absolute;top:31px;width:98px}
.footer-col h4{font-size:7px;font-weight:700;color:#fff;letter-spacing:.6px;margin-bottom:8px}
.footer-col a{display:block;font-size:7px;color:#aaa;height:18px;line-height:16px;border-bottom:1px dashed var(--footer-line);white-space:nowrap}
.footer-col a:last-child{border-bottom:0}
.ask-btn{position:absolute;left:482px;width:161px;height:20px;background:var(--gold);color:#fff;font-size:7.6px;line-height:20px;padding-left:10px;display:flex;align-items:center;gap:8px}
.footer-rule{position:absolute;left:57px;top:139px;width:586px;height:1px;background:var(--footer-line)}
.copyright{position:absolute;left:57px;top:152px;font-size:7px;color:#ddd}
</style>
</head>
<body>

<header class="site-header">
  <div class="brand"><span class="brand-mark"></span>Vemply Plinketra</div>
  <div class="topbar">
    <span class="support">Support : <span>info@plinketra.com</span></span><span>|</span><span>Register</span><span>|</span><span>Login</span>
  </div>
  <nav class="main-nav"><span>HOME</span><span>ABOUT US</span><span>FAQ</span><span>DDOS</span><span>CONTACT US</span></nav>
  <div class="search-field"></div>
  <div class="search-btn">Search</div>
</header>

<section class="hero">
  <div class="hero-photo" role="img" aria-label="Server room corridor opening onto a cloudy city skyline"></div>
  <div class="hero-caption">HIGH DENSITY, STATE OF THE ART OPENCELL CONTAINERS</div>
  <div class="hero-dots"><i></i><i class="on"></i><i></i></div>
</section>

<h2 class="section-title" style="top:324px">WELCOME TO OUR SITE</h2>
<p class="welcome-text">OpenCell is container-based virtualization for Linux. OpenCell creates multiple secure, isolated Linux containers (otherwise known as VEs or VPSs) on a single physical server enabling better server utilization. One of the main criticisms about OpenCell is that it's easy for providers to overcommit resources (aka "Overselling"), but when it's done right the virtualization (technically a context separation) offered by OpenCell offers near bare metal performances.</p>

<div class="spec" style="left:192px"><svg width="32" height="32" viewBox="0 0 32 32"><circle cx="16" cy="16" r="15" fill="none" stroke="#d4a21a"/><path d="M11 15l4 5 6-10" fill="none" stroke="#d4a21a"/></svg>4 CPU CORES</div>
<div class="spec" style="left:271px"><svg width="32" height="32" viewBox="0 0 32 32"><circle cx="16" cy="16" r="15" fill="none" stroke="#d4a21a"/><path d="M11 15l4 5 6-10" fill="none" stroke="#d4a21a"/></svg>4 GB RAM</div>
<div class="spec" style="left:349px"><svg width="32" height="32" viewBox="0 0 32 32"><circle cx="16" cy="16" r="15" fill="none" stroke="#d4a21a"/><path d="M11 15l4 5 6-10" fill="none" stroke="#d4a21a"/></svg>40 GB DISK</div>
<div class="spec" style="left:429px"><svg width="32" height="32" viewBox="0 0 32 32"><circle cx="16" cy="16" r="15" fill="none" stroke="#d4a21a"/><path d="M11 15l4 5 6-10" fill="none" stroke="#d4a21a"/></svg>2000 GB TRAFFIC</div>

<div class="laptop-art" role="img" aria-label="Laptop showing a blog page layout"></div>
<h3 class="features-title">FEATURES</h3>
<p class="features-intro">OpenCell is container-based virtualization for Linux. OpenCell creates multiple secure, isolated Linux containers (</p>
<ul class="feature-list" style="left:372px">
  <li>4 CPU CORES</li><li>4 GB RAM</li><li>40 GB DISK</li><li>2000 GB TRAFFIC</li><li>LINUX OPERATING SYSTEM</li><li>TUN / TAP / PPP / FUSE</li><li>1 IPV4, 4 IPV6</li><li>SHARED GIGABIT SPEED</li>
</ul>
<ul class="feature-list" style="left:507px">
  <li>VIRTUPANEL CONTROL PANEL</li><li>LOCATION: MILAN, ITALY</li><li>TEST IP 198.51.100.24</li><li>UNMANAGED SERVICE</li><li>NO REFUND</li><li>ONLY FOR GBP</li>
</ul>

<section class="plans">
  <h2 class="section-title" style="top:17px">PLANS</h2>
  <div class="plan-card" style="left:134px">
    <div class="price"><sup>$</sup>15</div><div class="per">PER MONTH</div>
    <div class="plan-name">ADVANCED PLAN</div>
    <ul class="perks"><li>10GB Disk Space</li><li>1TB Bandwidth</li><li>Free DDoS Protection</li><li>Free Daily Backups</li><li>Managed Hosting</li></ul>
    <div class="signup">SIGNUP</div>
  </div>
  <div class="plan-card" style="left:280px">
    <div class="price"><sup>$</sup>18</div><div class="per">PER MONTH</div>
    <div class="plan-name">BUSINESS PLAN</div>
    <ul class="perks"><li>10GB Disk Space</li><li>1TB Bandwidth</li><li>Free DDoS Protection</li><li>Free Daily Backups</li><li>Managed Hosting</li></ul>
    <div class="signup">SIGNUP</div>
  </div>
  <div class="plan-card gold" style="left:426px">
    <div class="price"><sup>$</sup>34</div><div class="per">PER MONTH</div>
    <div class="plan-name">GOLD PLAN</div>
    <ul class="perks"><li>10GB Disk Space</li><li>1TB Bandwidth</li><li>Free DDoS Protection</li><li>Free Daily Backups</li><li>Managed Hosting</li></ul>
    <div class="signup">SIGNUP</div>
  </div>
</section>

<footer class="site-footer">
  <div class="footer-col" style="left:59px"><h4>CHOOSE</h4><a>Share Hosting</a><a>Reseller Hosting</a><a>Cloud managed VPS</a><a>Managed Dedicated Servers</a></div>
  <div class="footer-col" style="left:199px"><h4>GET SUPPORT</h4><a>Contact Us</a><a>Knowledge Base</a><a>Submit a Ticke</a></div>
  <div class="footer-col" style="left:349px"><h4>START</h4><a>Blogpress Hosting</a><a>Portalo Hosting</a><a>Shopmage Hosting</a><a>Nodal Hosting</a></div>
  <div class="footer-col" style="left:482px"><h4>ASK</h4></div>
  <div class="ask-btn" style="top:51px"><svg width="9" height="8" viewBox="0 0 9 8"><ellipse cx="4.5" cy="3.5" rx="4.5" ry="3" fill="#fff"/></svg>Live Chat</div>
  <div class="ask-btn" style="top:76px"><svg width="8" height="8" viewBox="0 0 8 8"><path d="M1 0h2l1 2-1 1a5 5 0 0 0 2 2l1-1 2 1v2c-4 1-8-3-7-7z" fill="#fff"/></svg>41.2870.516</div>
  <div class="ask-btn" style="top:101px"><svg width="9" height="7" viewBox="0 0 9 7"><rect width="9" height="7" fill="#fff"/><path d="M0 0l4.5 4 4.5-4" fill="none" stroke="#d4a21a"/></svg>Email us</div>
  <div class="footer-rule"></div>
  <div class="copyright">©2015 plinketra - Terms of Service - Privacy - Program Policies</div>
</footer>

</body>
</html>
```